Ridgeline Orchards Organic Cherry POS card 7x11

We are wanting to create a one-sided 7 x 11 organic cherry card that is eye catching and informative.This should be clear and easy to read and not cluttered. We use these cards as a display in grocery stores, demo stands, and other events to market Organic Ridgeline Sweet Orchards. We have a few facts that we would like displayed on the card (see attachment).

Target Market(s)

Consumers

Industry/Entity Type

Agriculture

Requirements
Must have
• Natural color palettes
• Easy to read
• Ridgeline Orchards
Nice to have
• Unique, realistic cherry design

```html
<!DOCTYPE html>
<html lang="en">
<head>
<meta charset="utf-8">
<title>Ridgeline Orchards – Organic Cherry Card</title>
<link href="https://fonts.googleapis.com/css2?family=Josefin+Sans:wght@600&family=Dancing+Script:wght@500&display=swap" rel="stylesheet">
<style>
  :root {
    --paper: #ffffff;
    --blush: #f59ca2;
    --blush-light: #f8b3b7;
    --leaf: #8a9b3c;
    --ink: #2a1719;
    --cream: #ffffff;
    --cherry: #d0121b;
    --cherry-deep: #8e0a10;
  }
  * { margin: 0; padding: 0; box-sizing: border-box; }
  html, body {
    width: 1200px; height: 880px; overflow: hidden;
    background: var(--paper);
  }
  .card {
    position: absolute; left: 0; top: 58px;
    width: 1200px; height: 764px;
    background: radial-gradient(ellipse at 70% 30%, var(--blush-light), var(--blush) 70%);
    overflow: hidden;
  }
  .card__band { position: absolute; left: 0; top: 0; width: 1200px; height: 764px; }
  .fact {
    position: absolute;
    font-family: "Josefin Sans", sans-serif;
    font-weight: 600;
    font-size: 29px;
    line-height: 58px;
    letter-spacing: 0.34em;
    color: var(--ink);
    text-transform: uppercase;
  }
  .fact--share { left: 36px; top: 40px; }
  .fact--state { right: 44px; top: 394px; text-align: right; line-height: 44px; }
  .cherry-photo {
    position: absolute; left: 376px; top: 182px;
    width: 360px; height: 320px;
    border-radius: 46% 46% 40% 40%;
    background: radial-gradient(ellipse at 50% 70%, var(--cherry) 0%, var(--cherry-deep) 55%, rgba(245,156,162,0) 72%);
  }
  .benefits {
    position: absolute; left: 776px; top: 50px;
    width: 280px; height: 280px;
    border: 3px solid rgba(255,255,255,0.55);
    border-radius: 50%;
  }
  .benefits__list {
    position: absolute; left: 700px; top: 48px; width: 400px;
    list-style: none; text-align: center;
    font-family: "Dancing Script", cursive;
    font-weight: 500;
    font-size: 25px; line-height: 43px;
    color: var(--cream);
  }
  .benefits__arrow { position: absolute; left: 712px; top: 238px; }
  .brand {
    position: absolute; left: 34px; top: 606px;
    display: flex; align-items: center; gap: 22px;
    font-family: "Josefin Sans", sans-serif;
    font-weight: 600; font-size: 50px; letter-spacing: 0.02em;
    color: var(--cream);
  }
  .brand__dot {
    width: 96px; height: 96px; border-radius: 50%;
    border: 4px solid var(--cream);
  }
</style>
</head>
<body>
  <main class="card">
    <svg class="card__band" viewBox="0 0 1200 764" aria-hidden="true">
      <polygon points="0,450 1200,764 0,764" fill="var(--leaf)"/>
    </svg>

    <p class="fact fact--share">Organic<br>Ridgeline Orchards<br>make up 1/3<br>of the nation’s<br>production.</p>

    <div class="cherry-photo" role="img" aria-label="Photo of two red cherries with stems curled into a heart"></div>

    <div class="benefits"></div>
    <ul class="benefits__list">
      <li>Health benefits:</li>
      <li>fat free</li>
      <li>source of vitamin C</li>
      <li>a natural anti-inflammatory</li>
      <li>source of potassium</li>
      <li>source of melatonin</li>
    </ul>
    <svg class="benefits__arrow" width="90" height="50" viewBox="0 0 90 50" aria-hidden="true">
      <path d="M86 4 Q40 12 8 40" fill="none" stroke="var(--cream)" stroke-width="2.5" stroke-linecap="round"/>
      <path d="M6 26 L8 40 L22 40" fill="none" stroke="var(--cream)" stroke-width="2.5" stroke-linecap="round" stroke-linejoin="round"/>
    </svg>

    <p class="fact fact--state">Washington state<br>is the nation’s<br>largest producer<br>of organic<br>cherries.</p>

    <div class="brand">
      <span class="brand__dot"></span>
      <span class="brand__name">Ridgeline Orchards</span>
    </div>
  </main>
</body>
</html>
```